Cedarline Coalition Web Presence Design and Relaunch

Take existing web files and "clean up" for a a more presentable web landing pad.
posted presently on a site pad CSS template. at www.cedarlinecoalition.org

The site is clunky and unprofessional looking. Needs to be toned down so the urgency is conveyed, but not via a burning planet image.

Target Market(s)

Non-profit climate adaptation group targeting local government land management agencies, special districts and private landholders of natural resource properties.

Industry/Entity Type

Environment

Coding

Coded - Design and coding required

Number of Pages Required

Font styles to use
Serif
Sans Serif

Requirements
Must have
• Include current logos, aspects if content on current site www.cedarlinecoalition.org
• A regional Pacific Northwest Focus (US & Canada). Content speaking to urgency but respectful of cultural diversity and norms. Sustainability themes. Emphasis on action and implementation.
Nice to have
• link to like minded projects. Appear to future generations. Diversity in thematic areas ecological resiliency, energy, food security and infrastructure.

```html
<!DOCTYPE html>
<html lang="en">
<head>
<meta charset="utf-8">
<title>Cedarline Coalition</title>
<link href="https://fonts.googleapis.com/css2?family=Libre+Baskerville&family=Montserrat:wght@400;500;600&display=swap" rel="stylesheet">
<style>
:root{
  --blue:#0f8fd6;
  --green:#9dcb3b;
  --green-dark:#76b82a;
  --ink:#2f2f2f;
  --muted:#555;
  --card:#f0f0f0;
  --footer:#2b2b2b;
  --line:#cfcfcf;
}
*{margin:0;padding:0;box-sizing:border-box}
html,body{width:1200px;height:3516px;overflow:hidden;background:#fff}
body{position:relative;font-family:"Montserrat",sans-serif;color:var(--ink)}
.abs{position:absolute}
.serif{font-family:"Libre Baskerville",serif}

/* header */
.brand{left:72px;top:28px;display:flex;align-items:center;gap:10px}
.brand-dot{width:34px;height:34px;border-radius:50%;background:var(--green)}
.brand-name{font-family:"Montserrat",sans-serif;font-weight:600;font-size:20px;line-height:1.1;color:var(--blue);width:130px}
.nav{top:48px;left:438px;display:flex;gap:0;font-size:14px}
.nav a{color:#444;text-decoration:none;position:absolute;white-space:nowrap}
.nav a.active{color:var(--blue);font-weight:600}
.nav a.active::after{content:"";position:absolute;left:0;right:0;bottom:-22px;height:2px;background:var(--blue)}
.btn{display:flex;align-items:center;justify-content:center;background:var(--blue);color:#fff;border-radius:22px;font-size:14px;text-decoration:none}
.join{left:955px;top:36px;width:170px;height:40px}

/* hero */
.hero{left:0;top:110px;width:1200px;height:620px;background:radial-gradient(circle at 33% 45%,#e8e49a 0,#8fa84a 10%,#3f6a2c 26%,#22401f 60%,#1a3119 100%)}
.hero-label{left:685px;top:306px;font-size:12px;color:#fff}
.hero-title{left:685px;top:330px;font-size:36px;color:#fff}
.hero-text{left:685px;top:384px;width:320px;font-size:13px;line-height:16px;color:#fff}
.read{left:683px;top:456px;width:170px;height:38px;font-size:15px}
.arrow{top:395px;color:#9aa;font-size:24px}
.dots{left:577px;top:648px;display:flex;gap:7px}
.dots i{width:7px;height:7px;border-radius:50%;background:#bbb}
.dots i.on{background:#fff}

/* section titles */
.section-title{width:1200px;left:0;text-align:center;font-size:28px;color:#333}
.divider{left:550px;top:798px}

/* featured */
.card{top:864px;width:244px;height:261px;background:var(--card);text-align:center}
.card.hl{background:var(--green)}
.card svg.icon{margin-top:28px}
.card h3{font-family:"Libre Baskerville",serif;font-weight:400;font-size:17px;margin-top:12px;color:#333}
.card .bar{width:58px;height:3px;background:var(--blue);margin:14px auto 16px}
.card p{font-size:13px;line-height:16px;color:#444;padding:0 14px}
.card .go{margin-top:14px}
.card.hl h3,.card.hl p{color:#fff}
.card.hl .bar{background:#fff}

/* video */
.video{left:0;top:1199px;width:1200px;height:468px;background:linear-gradient(100deg,#9aa67c 0%,#c7cdb6 45%,#d6d8d4 60%,#a7b0a3 100%)}
.play{left:560px;top:1398px;width:86px;height:60px;border-radius:14px;background:#fff;opacity:.92}

/* recent */
.work{top:1784px;width:253px;height:236px}
.caption{width:253px;text-align:center}
.caption h4{font-family:"Libre Baskerville",serif;font-weight:400;font-size:16px;color:#333}
.caption span{font-size:12.5px;color:#555}

/* stats */
.stats{left:0;top:2124px;width:1200px;height:228px;background:linear-gradient(120deg,#86c230 0%,#71b22a 35%,#8cc63a 70%,#a3cf45 100%)}
.stat{width:260px;text-align:center;color:#fff}
.stat h5{font-family:"Libre Baskerville",serif;font-weight:400;font-size:16px;margin-top:14px}
.stat b{display:block;font-family:"Libre Baskerville",serif;font-weight:400;font-size:14px;margin-top:16px}

/* skills */
.skill-label{left:75px;font-family:"Libre Baskerville",serif;font-size:20px;color:#333}
.track{left:75px;width:494px;height:34px;background:#eee}
.fill{height:100%;background:var(--green)}
.pct{right:12px;top:8px;font-size:16px;color:#333}
.think-title{left:630px;top:2421px;font-size:27px;color:#333}
.think-img{left:631px;top:2465px;width:494px;height:289px;background:radial-gradient(circle at 55% 55%,#7fb7c8 0,#6f9a6a 22%,#cfc9bf 50%,#e9e6e1 80%)}

/* contact */
.field{height:32px;border:1px solid var(--line);font-size:12px;color:#777;padding:8px 14px}
.send{left:515px;top:3044px;width:170px;height:40px;font-size:15px}

/* footer */
.footer{left:0;top:3150px;width:1200px;height:306px;background:var(--footer)}
.f-brand{left:72px;top:3290px;color:#fff;font-weight:600;font-size:22px;line-height:1.15;width:160px}
.f-head{font-size:17px;color:#fff;font-weight:500}
.f-head::after{content:"";display:block;width:50px;height:2px;background:var(--green);margin-top:8px}
.f-list{list-style:none;font-size:13px;color:#fff;line-height:22.5px}
.f-list li::before{content:"•";margin-right:8px}
.f-contact{font-size:12.5px;color:#fff;line-height:24px}
.f-contact div{display:flex;gap:10px;align-items:flex-start}
.news-text{left:859px;top:3270px;width:270px;font-size:12.5px;line-height:15px;color:#fff}
.news-input{left:857px;top:3320px;width:269px;height:36px;border-radius:18px;background:#fff;font-size:12px;color:#999;padding:11px 14px}
.subscribe{left:857px;top:3365px;width:269px;height:36px;border-radius:18px;background:var(--green);color:#333;font-size:12px;display:flex;align-items:center;justify-content:center}
.bottom{left:0;top:3456px;width:1200px;height:60px;background:#fff}
.copy{left:75px;top:3476px;font-size:12.5px;color:#333}
.social{top:3470px;width:29px;height:29px;border-radius:50%;background:#222}
.social.first{background:var(--blue)}
</style>
</head>
<body>

<!-- header -->
<div class="abs brand"><span class="brand-dot"></span><span class="brand-name">Cedarline Coalition</span></div>
<nav class="abs nav">
  <a class="active" style="left:0">Home</a>
  <a style="left:81px">About us</a>
  <a style="left:182px">Featured</a>
  <a style="left:285px">Recent Work</a>
  <a style="left:413px">Contact us</a>
</nav>
<a class="abs btn join">Join us Today</a>

<!-- hero -->
<div class="abs hero" role="img" aria-label="Hand holding a glowing light bulb plant surrounded by circular clean energy icons on a leafy green background"></div>
<div class="abs hero-label serif">Limate Adaptation Implementing</div>
<h1 class="abs hero-title serif" style="font-weight:400">Climate Strategies</h1>
<p class="abs hero-text">Dedicated to taking action the Cedarline Coalition was created to help bring adaption strategies to life.</p>
<a class="abs btn read">Read More</a>
<div class="abs arrow" style="left:16px">&#8592;</div>
<div class="abs arrow" style="left:1136px">&#8594;</div>
<div class="abs dots"><i></i><i class="on"></i><i></i><i></i></div>
<svg class="abs" style="left:0;top:640px" width="1200" height="100" viewBox="0 0 1200 100">
  <path d="M0 100 L0 78 C200 50 420 55 640 62 C860 70 1040 60 1200 30 L1200 100Z" fill="#fff"/>
  <path d="M0 92 C120 66 260 48 430 48 C260 52 120 70 0 62Z" fill="#0f8fd6"/>
  <path d="M865 75 C1000 70 1120 50 1200 30 L1200 42 C1110 66 1000 76 865 75Z" fill="#9dcb3b"/>
</svg>

<!-- featured -->
<h2 class="abs section-title serif" style="top:750px;font-weight:400">Featured Projects</h2>
<svg class="abs divider" width="100" height="34" viewBox="0 0 100 34">
  <line x1="0" y1="28" x2="100" y2="28" stroke="#0f8fd6" stroke-width="1.5"/>
  <circle cx="50" cy="12" r="10" fill="#9dcb3b"/>
  <line x1="50" y1="16" x2="50" y2="30" stroke="#0f8fd6" stroke-width="2"/>
</svg>

<div class="abs card" style="left:77px">
  <svg class="icon" width="64" height="64" viewBox="0 0 64 64" fill="none" stroke="#222" stroke-width="2"><circle cx="32" cy="36" r="22"/><path d="M10 36h44M32 14c-10 12-10 32 0 44M32 14c10 12 10 32 0 44"/></svg>
  <h3>Adaptation Plans</h3><div class="bar"></div>
  <p>Communities throughout the region have adopted plans to address our changing climate.</p>
  <svg class="go" width="20" height="20" viewBox="0 0 20 20" fill="none" stroke="#222" stroke-width="2"><circle cx="10" cy="10" r="8"/><path d="M8 6l4 4-4 4"/></svg>
</div>
<div class="abs card" style="left:345px">
  <svg class="icon" width="64" height="64" viewBox="0 0 64 64" fill="none" stroke="#222" stroke-width="2"><path d="M32 6C22 22 14 32 14 42a18 18 0 0 0 36 0C50 32 42 22 32 6z"/><path d="M26 50c0-10 6-16 14-18M30 44c4 0 8-4 8-8"/></svg>
  <h3>On The Ground</h3><div class="bar"></div>
  <p>Communities throughout the region have adopted plans to address our changing climate.</p>
  <svg class="go" width="20" height="20" viewBox="0 0 20 20" fill="none" stroke="#222" stroke-width="2"><circle cx="10" cy="10" r="8"/><path d="M8 6l4 4-4 4"/></svg>
</div>
<div class="abs card hl" style="left:613px">
  <svg class="icon" width="64" height="64" viewBox="0 0 64 64" fill="none" stroke="#fff" stroke-width="2"><path d="M34 30c0-10 6-18 18-20 0 12-8 20-18 20zM34 30c0-8-6-14-14-14 0 8 6 14 14 14zM34 30v12"/><path d="M6 42h10v16H6zM16 46h14c4 0 6 4 2 6l-8 1M16 56h22l18-10c2-2 0-6-4-4l-12 6"/></svg>
  <h3>Ecological Resilence</h3><div class="bar"></div>
  <p>Communities throughout the region have adopted plans to address our changing climate.</p>
  <svg class="go" width="20" height="20" viewBox="0 0 20 20" fill="none" stroke="#fff" stroke-width="2"><circle cx="10" cy="10" r="8"/><path d="M8 6l4 4-4 4"/></svg>
</div>
<div class="abs card" style="left:882px">
  <svg class="icon" width="64" height="64" viewBox="0 0 64 64" fill="none" stroke="#222" stroke-width="2"><circle cx="32" cy="34" r="16"/><path d="M34 24l-6 11h8l-6 11M32 6v8M32 54v8M4 34h8M52 34h8M12 14l6 6M52 14l-6 6M12 54l6-6M52 54l-6-6"/></svg>
  <h3>Energy and Food</h3><div class="bar"></div>
  <p>Communities throughout the region have adopted plans to address our changing climate.</p>
  <svg class="go" width="20" height="20" viewBox="0 0 20 20" fill="none" stroke="#222" stroke-width="2"><circle cx="10" cy="10" r="8"/><path d="M8 6l4 4-4 4"/></svg>
</div>

<!-- video -->
<div class="abs video" role="img" aria-label="Two cupped hands, one holding a small tree and the other holding the Earth with a butterfly on top"></div>
<svg class="abs play" width="86" height="60" viewBox="0 0 86 60"><path d="M34 18l20 12-20 12z" fill="#333"/></svg>

<!-- recent work -->
<h2 class="abs section-title serif" style="top:1724px;font-weight:400">Recent Work</h2>
<div class="abs work" style="left:75px;background:linear-gradient(180deg,#8a98a8 0%,#c9a56a 55%,#b77a2c 80%,#6a5a2a 100%)" role="img" aria-label="Wind turbines on golden hills at sunset"></div>
<div class="abs work" style="left:341px;background:linear-gradient(180deg,#e8ede8 0%,#c7d8b6 35%,#5c9a2e 60%,#2f6a1c 100%)" role="img" aria-label="Rows of green crops inside a greenhouse"></div>
<div class="abs work" style="left:607px;background:linear-gradient(180deg,#8ba663 0%,#5f7e3c 50%,#3d3326 75%,#2a231b 100%)" role="img" aria-label="Young seedlings sprouting from dark soil"></div>
<div class="abs work" style="left:873px;background:linear-gradient(160deg,#b9b89a 0%,#7d9880 40%,#5e7a73 70%,#8b9a94 100%)" role="img" aria-label="Aerial view of highway interchanges and city infrastructure"></div>
<div class="abs caption" style="left:75px;top:2040px"><h4>Energy</h4><span>Investing in clean energy</span></div>
<div class="abs caption" style="left:341px;top:2040px"><h4>Food Security</h4><span>Retooling agriculture/span</span></div>
<div class="abs caption" style="left:607px;top:2040px"><h4>Ecological Resilience</h4><span>Environmental Progress</span></div>
<div class="abs caption" style="left:873px;top:2040px"><h4>Infrastructure</h4><span>Lorem Ipsum</span></div>

<!-- stats -->
<div class="abs stats"></div>
<div class="abs stat" style="left:101px;top:2172px">
  <svg width="64" height="64" viewBox="0 0 64 64" fill="none" stroke="#fff" stroke-width="2"><circle cx="32" cy="36" r="22"/><path d="M10 36h44M32 14c-10 12-10 32 0 44M32 14c10 12 10 32 0 44"/></svg>
  <h5>Projects Completed</h5><b>250 +</b>
</div>
<div class="abs stat" style="left:368px;top:2172px">
  <svg width="64" height="64" viewBox="0 0 64 64" fill="none" stroke="#fff" stroke-width="2"><path d="M44 30C34 22 30 16 34 10c3-4 8-3 10 1 2-4 7-5 10-1 4 6 0 12-10 20z"/><path d="M6 42h10v16H6zM16 46h14c4 0 6 4 2 6l-8 1M16 56h22l18-10c2-2 0-6-4-4l-12 6"/></svg>
  <h5>Donations</h5><b>300 +</b>
</div>
<div class="abs stat" style="left:619px;top:2172px">
  <svg width="64" height="64" viewBox="0 0 64 64" fill="none" stroke="#fff" stroke-width="2"><path d="M18 8h28v14a14 14 0 0 1-28 0zM18 12H8c0 10 4 14 10 14M46 12h10c0 10-4 14-10 14M32 36v12M22 56h20l-2-8H24z"/><path d="M32 12l3 6 6 1-4 4 1 6-6-3-6 3 1-6-4-4 6-1z"/></svg>
  <h5>Communities Engaged</h5><b>17 +</b>
</div>
<div class="abs stat" style="left:867px;top:2172px">
  <svg width="64" height="64" viewBox="0 0 64 64" fill="none" stroke="#fff" stroke-width="2"><circle cx="32" cy="26" r="6"/><circle cx="14" cy="36" r="6"/><circle cx="50" cy="36" r="6"/><path d="M4 60v-6a10 10 0 0 1 20 0v6zM40 60v-6a10 10 0 0 1 20 0v6zM22 50v-4a10 10 0 0 1 20 0v4M32 4v8M20 8l4 6M44 8l-4 6"/></svg>
  <h5>Volunteers</h5><b>70 +</b>
</div>

<!-- skills -->
<div class="abs skill-label" style="top:2432px">Clean Water</div>
<div class="abs track" style="top:2467px"><div class="fill" style="width:418px"></div><span class="abs pct">98%</span></div>
<div class="abs skill-label" style="top:2521px">Forest Rescue</div>
<div class="abs track" style="top:2554px"><div class="fill" style="width:197px"></div><span class="abs pct">56%</span></div>
<div class="abs skill-label" style="top:2606px">Agriculture</div>
<div class="abs track" style="top:2640px"><div class="fill" style="width:284px"></div><span class="abs pct">77%</span></div>
<div class="abs skill-label" style="top:2688px">Alternative Energy</div>
<div class="abs track" style="top:2722px"><div class="fill" style="width:358px"></div><span class="abs pct">84%</span></div>

<h2 class="abs think-title serif" style="font-weight:400">Think Green ! Save Money</h2>
<div class="abs think-img" role="img" aria-label="Two hands cradling a small world of trees, waterfalls and clouds with birds flying around"></div>

<!-- contact -->
<h2 class="abs section-title serif" style="top:2828px;font-weight:400">Contact us</h2>
<div class="abs field" style="left:288px;top:2878px;width:201px">Name*</div>
<div class="abs field" style="left:503px;top:2878px;width:201px">Phone*</div>
<div class="abs field" style="left:716px;top:2878px;width:201px">Email*</div>
<div class="abs field" style="left:288px;top:2922px;width:629px;height:104px">Message</div>
<a class="abs btn send">Send Now</a>

<!-- footer -->
<svg class="abs" style="left:0;top:3080px" width="1200" height="80" viewBox="0 0 1200 80">
  <path d="M0 80 L0 70 C220 40 420 34 640 42 C860 52 1040 46 1200 20 L1200 80Z" fill="#2b2b2b"/>
  <path d="M0 78 C120 50 260 32 410 30 C260 36 120 50 0 54Z" fill="#0f8fd6"/>
  <path d="M775 56 C950 52 1100 34 1200 10 L1200 22 C1100 46 950 58 775 56Z" fill="#9dcb3b"/>
</svg>
<div class="abs footer"></div>
<div class="abs f-brand">Cedarline Coalition</div>

<div class="abs f-head" style="left:331px;top:3222px">Quick Link</div>
<ul class="abs f-list" style="left:333px;top:3270px">
  <li>Home</li><li>About us</li><li>Featured</li><li>Recent Work</li><li>Contact us</li>
</ul>

<div class="abs f-head" style="left:547px;top:3222px">Quick Contact</div>
<div class="abs f-contact" style="left:547px;top:3266px">
  <div><svg width="12" height="16" viewBox="0 0 12 16" style="margin-top:4px" fill="none" stroke="#fff" stroke-width="1.5"><path d="M6 15s5-5 5-9a5 5 0 0 0-10 0c0 4 5 9 5 9z"/><circle cx="6" cy="6" r="2"/></svg><span>2180 Fernridge Rd, Alder<br>Bay WA 98201</span></div>
  <div style="margin-top:22px"><svg width="14" height="12" viewBox="0 0 14 12" style="margin-top:6px" fill="none" stroke="#fff" stroke-width="1.3"><rect x="1" y="3" width="12" height="8"/><path d="M3 3V1h8v2"/></svg><span>360-555-0187</span></div>
  <div><svg width="14" height="12" viewBox="0 0 14 12" style="margin-top:6px" fill="none" stroke="#fff" stroke-width="1.3"><rect x="1" y="1" width="12" height="10"/><path d="M1 1l6 5 6-5"/></svg><span>info@cedarlinecoalition.org</span></div>
</div>

<div class="abs f-head" style="left:860px;top:3222px">Join Our Newletter</div>
<p class="abs news-text">Lorem Ipsum is simply dummy the printing and typesetting industry.</p>
<div class="abs news-input">Email Here</div>
<div class="abs subscribe">SUBSCRIBE</div>

<div class="abs bottom"></div>
<div class="abs copy">Copyright © 2020 Cedarline Coalition. All Right Reserved</div>
<span class="abs social first" style="left:970px"></span>
<span class="abs social" style="left:1012px"></span>
<span class="abs social" style="left:1054px"></span>
<span class="abs social" style="left:1097px"></span>

</body>
</html>
```